Menu Guide/Magazine

We are a restaurant meal delivery service. We currently deliver for 9 restaurants and would like to have a magazine with each restaurants having 1 page each. We are looking for a design for the front and back cover and a template design for two of the menus for the restaurants that we deliver for.

The website is www.brisklarkmeals.com

Industry/Entity Type

Restaurant

```html
<!DOCTYPE html>
<html lang="en">
<head>
<meta charset="utf-8">
<title>Navratan Menu</title>
<link rel="stylesheet" href="https://fonts.googleapis.com/css2?family=Questrial&family=Cabin:wght@400;500&family=Arimo:ital,wght@0,400;0,700;1,400&family=Lobster&display=swap">
<style>
:root{
  --paper:#efefed;
  --red:#b5161c;
  --band:#a81d22;
  --ink:#1b1b1b;
  --muted:#3a3a3a;
  --white:#ffffff;
  --rule:#c9c9c6;
}
*{box-sizing:border-box;margin:0;padding:0}
html,body{width:1200px;height:776px;overflow:hidden;background:var(--paper)}
.menu{position:relative;width:1200px;height:776px;background:var(--paper);font-family:"Arimo",Arial,sans-serif;color:var(--ink)}
.edge-mark{position:absolute;top:30px;width:12px;height:26px;background:var(--band)}
.edge-mark.left{left:0}.edge-mark.right{right:0}
.brand-title{position:absolute;left:28px;top:24px;font-family:"Questrial",sans-serif;font-weight:400;font-size:38px;letter-spacing:1px;line-height:40px}
.address{position:absolute;left:240px;top:33px;font-weight:700;font-size:12px;line-height:15px}
.brand-mark{position:absolute;left:405px;top:33px;display:flex;align-items:center;gap:6px;font-family:"Questrial",sans-serif;font-size:20px}
.brand-mark .square{width:22px;height:22px;background:var(--ink)}
.hours{position:absolute;left:628px;top:26px;display:flex}
.hours-label{width:44px;font-size:8px;font-weight:700;font-style:italic;color:var(--red);line-height:10px;padding-top:2px}
.hours-day{width:73px;text-align:center;font-size:8px;line-height:9px}
.hours-day .day{font-size:10px;font-style:italic;line-height:13px}
.rule{position:absolute;left:28px;right:28px;top:72px;border-top:1px solid var(--rule)}

.column{position:absolute;top:85px;display:flex;flex-direction:column}
.col-1{left:28px;width:155px}
.col-2{left:222px;width:173px}
.col-3{left:417px;width:188px}
.col-4{left:628px;width:155px}
.col-5{left:822px;width:173px}
.col-6{left:1018px;width:154px}

.heading{font-family:"Cabin",sans-serif;font-weight:400;font-size:20px;color:var(--red);line-height:22px;margin-bottom:3px;white-space:nowrap;letter-spacing:-0.2px}
.note{font-size:9px;font-style:italic;color:var(--red);line-height:11px;margin:-1px 0 7px}
.item{margin-bottom:6px}
.row{display:flex;align-items:flex-end;font-weight:700;font-size:11px;line-height:13px}
.row .fill{flex:1;border-bottom:1px solid #555;margin:0 4px 3px}
.desc{font-size:7.5px;font-style:italic;line-height:8.5px;color:var(--muted)}

.photo{border-radius:4px;flex:none}
.photo.samosa{width:154px;height:80px;margin:4px 0 12px;background:linear-gradient(135deg,#d9a24a,#b86a2a 55%,#6a8a3a)}
.photo.curry{width:155px;height:90px;margin-top:8px;background:radial-gradient(ellipse at center,#c9532a,#a8782f 60%,#e6e3dc)}
.photo.sweets{width:154px;height:126px;margin:6px 0 18px;background:linear-gradient(160deg,#f2efe8,#e7b27a 55%,#b98b5c)}
.gap-s{margin-top:8px}
.gap-m{margin-top:14px}

.band{position:absolute;left:28px;top:724px;width:1144px;height:38px;background:var(--band);border-radius:8px;display:flex;align-items:center;color:var(--white);font-family:"Lobster",cursive}
.band-brand{display:flex;align-items:center;gap:6px;margin-left:12px;font-size:20px;width:170px}
.band-brand .dot{width:14px;height:14px;border-radius:50%;background:var(--white)}
.band-phone{font-size:24px;margin-left:10px}
.band-web{font-size:22px;margin-left:auto;margin-right:16px}
</style>
</head>
<body>
<div class="menu">
  <div class="edge-mark left"></div><div class="edge-mark right"></div>
  <h1 class="brand-title">NAVRATAN</h1>
  <p class="address">2750 W. Maple Avenue,<br>Fairview, IL 60999</p>
  <div class="brand-mark"><span class="square"></span>Navratan</div>

  <div class="hours">
    <div class="hours-label">Open Delivery Hours</div>
    <div class="hours-day"><div class="day">Monday</div>Closed</div>
    <div class="hours-day"><div class="day">Tuesday</div>11:30AM - 2:00PM<br>4:30PM - 8:30PM</div>
    <div class="hours-day"><div class="day">Wednesday</div>11:30AM - 2:00PM<br>4:30PM - 8:30PM</div>
    <div class="hours-day"><div class="day">Thursday</div>11:30AM - 2:00PM<br>4:30PM - 8:30PM</div>
    <div class="hours-day"><div class="day">Friday</div>11:30AM - 2:00PM<br>4:30PM - 8:30PM</div>
    <div class="hours-day"><div class="day">Saturday</div>11:30AM - 2:00PM<br>4:30PM - 8:30PM</div>
    <div class="hours-day"><div class="day">Sunday</div>11:30AM - 2:00PM<br>4:30PM - 8:30PM</div>
  </div>
  <div class="rule"></div>

  <div class="column col-1">
    <section>
      <h2 class="heading">Appetizers</h2>
      <div class="item"><div class="row">Pakora<span class="fill"></span>$3.00</div><p class="desc">Assorted vegetables dipped in batter, mashed then pan fried in Canola Oil</p></div>
      <div class="item"><div class="row">Samosa<span class="fill"></span>$3.00</div><p class="desc">Deep fried cone pastry stuffed with potatoes &amp; green peas (2 pieces)</p></div>
      <div class="item"><div class="row">Aloo Tikki<span class="fill"></span>$4.00</div><p class="desc">Crisp patties made with a combination of potatoes &amp; spiced lentils</p></div>
      <div class="item"><div class="row">Appetizer Platter<span class="fill"></span>$8.95</div><p class="desc">Assorted samples of Pakoras, Kabobs, Aaloo Tikki, &amp; Chicken Tikka</p></div>
      <div class="item"><div class="row">Chicken Wings<span class="fill"></span>$8.00</div><p class="desc">Sizzling Hot Wings dipped in hot sauce (10 Pieces)</p></div>
    </section>
    <div class="photo samosa" role="img" aria-label="Photo of samosas with dipping sauces"></div>
    <section>
      <h2 class="heading">Soups &amp; Salads</h2>
      <div class="item"><div class="row">Tamatar Shorba<span class="fill"></span>$4.00</div><p class="desc">Savory exotically spiced herbed tomato soup</p></div>
      <div class="item"><div class="row">Mulligatawny Soup<span class="fill"></span>$4.50</div><p class="desc">Flavorful vegetables, chicken &amp;split peas subtly flavored with special herbs</p></div>
      <div class="item"><div class="row">Keera Raita<span class="fill"></span>$3.50</div><p class="desc">Yogurt with grated cucumbers</p></div>
      <div class="item"><div class="row">Navratan Salad<span class="fill"></span>$4.00</div><p class="desc">Chopped vegetables mixed with a lemon &amp; vinegar dressing</p></div>
      <div class="item"><div class="row">Green Salad<span class="fill"></span>$3.00</div><p class="desc">Lettuce, Tomatoes, Cucumbers, Onion</p></div>
    </section>
    <section class="gap-m">
      <h2 class="heading">Sandwich Wraps</h2>
      <p class="note">(Served with lettuce, onion &amp; raita served w/potatoe french fries)</p>
      <div class="item"><div class="row">Seekh Kobob Wrap<span class="fill"></span>$10.95</div><p class="desc">Finely seasoned minced beef sausage, grilled &amp; wrapped in Paratha.</p></div>
      <div class="item"><div class="row">Chicken Boti Wrap<span class="fill"></span>$10.95</div><p class="desc">Boneless chicken marinated in a blend of yogurt, ginger &amp; garlic grilled to perfection wrapped in Paratha.</p></div>
    </section>
  </div>

  <div class="column col-2">
    <section>
      <h2 class="heading">Indian Bread</h2>
      <p class="note">(Served Freshly Baked From Our Tandoor Clay Oven)</p>
      <div class="item"><div class="row">Naan<span class="fill"></span>$1.50</div><p class="desc">Oven baked flat bread made of super fine flour dough baked in Tandoor clay oven</p></div>
      <div class="item"><div class="row">Tandoori Roti<span class="fill"></span>$1.50</div><p class="desc">Whole-Wheat Rustic bread baked bread</p></div>
      <div class="item"><div class="row">Onion Kulcha<span class="fill"></span>$2.95</div><p class="desc">Super fine flour bread stuffed with a mix of Onions, green chilies &amp; coriander</p></div>
      <div class="item"><div class="row">Cheese Kulcha<span class="fill"></span>$2.95</div><p class="desc">Oven fresh baked bread stuffed homemade cheese</p></div>
      <div class="item"><div class="row">Poori<span class="fill"></span>$3.00</div><p class="desc">Round Whole-wheat bread puffs (2 pieces)</p></div>
      <div class="item"><div class="row">Aaloo Paratha<span class="fill"></span>$3.00</div><p class="desc">Whole-wheat bread with potatoes, onions &amp; spices</p></div>
      <div class="item"><div class="row">Plain Paratha<span class="fill"></span>$2.50</div></div>
    </section>
    <section class="gap-m">
      <h2 class="heading">Delicacies<br>from the Tandoor<br>(Clay Oven)</h2>
      <div class="item"><div class="row">Chicken Tikka<span class="fill"></span>$12.95</div><p class="desc">Delectable bite-sized chunks of boneless Chicken seasoned in a rich blend of Spices, lemon juice, yogurt; than char Grilled to perfection</p></div>
      <div class="item"><div class="row">Chicken Tandoori<br>(Bone In)-Half<span class="fill"></span>$8.95</div><p class="desc">Chicken marinated in a blend of yogurt, Ginger &amp; Garlic masterfully basted &amp; Barbequed over charcoal</p></div>
      <div class="item"><div class="row">Chicken Tandoori<br>(Bone In)-Full<span class="fill"></span>$12.95</div><p class="desc">Chicken marinated in a blend of yogurt, Ginger &amp; Garlic masterfully basted &amp; Barbequed over charcoal</p></div>
      <div class="item"><div class="row">Seekh Kabob<span class="fill"></span>$12.95</div><p class="desc">Minced lamb finely seasoned with delectable spices charcoal grilled on a skewer (Naan Bread Included)</p></div>
      <div class="item"><div class="row">Fish Tikka<span class="fill"></span>$13.95</div><p class="desc">Marinated piece of Talipia tenderly spiced</p></div>
      <div class="item"><div class="row">Tandoori Mix Grill<span class="fill"></span>$13.95</div><p class="desc">Assortment of items listed above (Naan Bread Included)</p></div>
    </section>
  </div>

  <div class="column col-3">
    <section>
      <h2 class="heading">Vegetarian<br>Delights</h2>
      <div class="item"><div class="row">Saag Paneer<span class="fill"></span>$10.95</div><p class="desc">Fresh homemade Indian cheese cubes in Spice creamed spinach</p></div>
      <div class="item"><div class="row">Bhindi Masala<span class="fill"></span>$10.95</div><p class="desc">Delicious Okra cooked with onions Tomatoes and spices</p></div>
      <div class="item"><div class="row">Vegetable Jalfraize<span class="fill"></span>$10.95</div><p class="desc">Stir-fried, lightly spiced with coriander red, green chillies &amp; cumin</p></div>
      <div class="item"><div class="row">Baigan Bhurta<span class="fill"></span>$10.95</div><p class="desc">Eggplant gently roasted in Tandoor, Mashed &amp; marinated in rich blend Of mughlai spices, cooked over low heat to draw the richness of the spices</p></div>
      <div class="item"><div class="row">Malai Kofta<span class="fill"></span>$10.95</div><p class="desc">Combination of potatoes, mixed vegetables, &amp; paneer delicious, creamy, savoury alternatives to meatballs</p></div>
      <div class="item"><div class="row">Muttar Paneer<span class="fill"></span>$10.95</div><p class="desc">Fresh homemade cheese cubes cooked with green peas</p></div>
      <div class="item"><div class="row">Chana Masala<span class="fill"></span>$10.95</div><p class="desc">Delicious chickpeas cooked in an exotic blend of North Indian spices</p></div>
      <div class="item"><div class="row">Dal Makhani<span class="fill"></span>$10.95</div><p class="desc">Black Lentils simmered on slow fire until tender; tempered with onions ginger, garlic &amp; tomatoes</p></div>
      <div class="item"><div class="row">Aaloo Gobhi<span class="fill"></span>$9.95</div><p class="desc">Spiced cauliflower, potatoes &amp; spring peas, sauteed in traditional North Indian style</p></div>
      <div class="item"><div class="row">Jeera Aaloo<span class="fill"></span>$10.95</div><p class="desc">Potatoes steamed &amp; sauteed with cumin seeds &amp; fresh herbs</p></div>
      <div class="item"><div class="row">Paneer Tikka Masala<span class="fill"></span>$10.95</div><p class="desc">Marinated Indian Cheese cubes in a flavorful curry tomato cream sauce</p></div>
      <div class="item"><div class="row">Kofta Curry<span class="fill"></span>$10.95</div><p class="desc">Combination of potato, mixed vegetables, &amp; paneer. Delicious, creamy, savory vegetable balls blended in aromatic spice curry</p></div>
      <div class="item"><div class="row">Green Beans<span class="fill"></span>$10.95</div><p class="desc">Lightly seasoned green beans served with potatoes.</p></div>
      <div class="item"><div class="row">Gobi Manchurian<span class="fill"></span>$10.95</div><p class="desc">Lightly breaded cauliflower tossed in tomato garlic green and red chilli sauce.</p></div>
    </section>
  </div>

  <div class="column col-4">
    <section>
      <h2 class="heading">Chicken Specialties</h2>
      <div class="item"><div class="row">Chicken Boti<span class="fill"></span>$11.95</div><p class="desc">Boneless Chicken marinated over night with yogurt, ginger &amp; garlic grilled to perfection</p></div>
      <div class="item"><div class="row">Kadhai Chicken<span class="fill"></span>$11.95</div><p class="desc">Chicken marinated with a spicy tomato based curry</p></div>
      <div class="item"><div class="row">Chicken Tikka Masala<span class="fill"></span>$11.95</div><p class="desc">Chunks of chicken roasted in a clay oven &amp; then folded into a tomato cream sauce</p></div>
      <div class="item"><div class="row">Palak Chicken<span class="fill"></span>$11.95</div><p class="desc">Chicken sauteed w/ spices in spinach</p></div>
      <div class="item"><div class="row">Chicken Vindaloo<span class="fill"></span>$11.95</div><p class="desc">Boneless chicken and potato cooked in a hot &amp; spicy onion tomato sauce</p></div>
      <div class="item"><div class="row">Chicken Makhani<span class="fill"></span>$11.95</div><p class="desc">Boneless tandoori chicken cooked in a light spiced tomato cream sauce</p></div>
      <div class="item"><div class="row">Chicken Korma<span class="fill"></span>$11.95</div><p class="desc">Chicken cubes cooked in a rich sauce w/ almonds</p></div>
      <div class="item"><div class="row">Chicken Curry<span class="fill"></span>$11.95</div><p class="desc">Boneless chicken simmered in tomato &amp; onion gravy w/ blend of aromatic spices</p></div>
      <div class="item"><div class="row">Chicken Manchurian<span class="fill"></span>$11.95</div><p class="desc">Lightly breaded chicken tossed in tomato garlic green and red chili sauce</p></div>
    </section>
    <section class="gap-s">
      <h2 class="heading">Beef Entrees</h2>
      <div class="item"><div class="row">Nehari<span class="fill"></span>$10.95</div><p class="desc">Special Pakistani dish w/ slowly cooked Chunks of beef in a spicy curry</p></div>
      <div class="item"><div class="row">Aloo Polak Keema<span class="fill"></span>$10.95</div><p class="desc">Ground beef richly spiced &amp; cooked w/ potatoes &amp; spinach</p></div>
      <div class="item"><div class="row">Beef Curry<span class="fill"></span>$10.95</div><p class="desc">Seasoned beef cooked to perfection in a spicy curry sauce</p></div>
      <div class="item"><div class="row">Beef Vindoloo<span class="fill"></span>$10.95</div><p class="desc">Combination of tender seasoned beef &amp; potatoes in a spiced curry sauce</p></div>
    </section>
    <div class="photo curry" role="img" aria-label="Photo of a curry dish in a copper bowl with naan"></div>
  </div>

  <div class="column col-5">
    <section>
      <h2 class="heading">Lamb Specialties</h2>
      <div class="item"><div class="row">Roghan Josh<span class="fill"></span>$12.95</div><p class="desc">Succulent pieces of lamb in a cardamom Flavored sauce</p></div>
      <div class="item"><div class="row">Lamb Vindaloo<span class="fill"></span>$12.95</div><p class="desc">Tender lamb cooked with potatoes &amp; spiced fiery hot</p></div>
      <div class="item"><div class="row">Kadhai Gosht<span class="fill"></span>$12.95</div><p class="desc">Boneless lamb cooked fresh tomatoes, onion garlic &amp; mild spices; garnished w/ fresh cilantro &amp; ginger</p></div>
      <div class="item"><div class="row">Saag Ghost<span class="fill"></span>$12.95</div><p class="desc">Cubes of lamb in a spicy spinach puree</p></div>
    </section>
    <section class="gap-m">
      <h2 class="heading">Seafood Specialties</h2>
      <div class="item"><div class="row">Shrimp Vindaloo<span class="fill"></span>$13.95</div><p class="desc">A combination of shrimp &amp; potatoes in spiced curry sauce</p></div>
      <div class="item"><div class="row">Fish Tikka Masala<span class="fill"></span>$13.95</div><p class="desc">Barbecue pieces of fish cooked w/ Indian Spice</p></div>
      <div class="item"><div class="row">Bombay Shrimp Curry<span class="fill"></span>$13.95</div><p class="desc">Shrimp cooked w/ bell peppers in spicy curry sauce</p></div>
      <div class="item"><div class="row">Fish Curry<span class="fill"></span>$13.95</div><p class="desc">Seasonal fish cooked w/ grated coconut</p></div>
    </section>
    <section class="gap-m">
      <h2 class="heading">Rice Specialties</h2>
      <div class="item"><div class="row">Steamed Basmati Rice<span class="fill"></span>$4.50</div><p class="desc">Fine quality long-grain rice</p></div>
      <div class="item"><div class="row">Vegetable Pulao<span class="fill"></span>$9.95</div><p class="desc">Aromatic saffron-flavored rice cooked w/ Fresh vegetables &amp; garnished with fresh herbs</p></div>
      <div class="item"><div class="row">Navratan Biryani<span class="fill"></span>$14.95</div><p class="desc">Basmati rice served with lamb, chicken tikka, &amp; shrimp</p></div>
      <div class="item"><div class="row">Chicken Biryani<span class="fill"></span>$11.95</div><p class="desc">Basmati rice flavored w/ saffron; cooked w/ chicken in a delicate blend herbs &amp; spices</p></div>
      <div class="item"><div class="row">Lamb Biryani<span class="fill"></span>$12.95</div><p class="desc">Basmati rice flavored w/ saffron; cooked w/ lamb in a delicate blend of herbs &amp; spices</p></div>
      <div class="item"><div class="row">Shrimp Biryani<span class="fill"></span>$13.95</div><p class="desc">Basmati rice flavored w/ saffron; cooked w/ shrimp in a delicate blend of savory spices</p></div>
    </section>
  </div>

  <div class="column col-6">
    <section>
      <h2 class="heading">Desserts</h2>
      <div class="item"><div class="row">Gulab Jamun<span class="fill"></span>$4.00</div><p class="desc">Golden fried balls of milk pastry soaked in sweet saffron syrup &amp; served warm</p></div>
      <div class="item"><div class="row">Carrot Halwa<span class="fill"></span>$4.00</div><p class="desc">Caramelized grated carrots, topped off w/ pistachios</p></div>
      <div class="item"><div class="row">Semolina Halwa<span class="fill"></span>$3.95</div><p class="desc">Sweet delicious dessert includes a mixture of cardamom, saffron, sugar and milk</p></div>
      <div class="item"><div class="row">Kheer<span class="fill"></span>$4.50</div><p class="desc">Flavorful Indian rice pudding made w/ Coconut milk, raisins &amp; nuts</p></div>
      <div class="item"><div class="row">Ras Malia<span class="fill"></span>$4.50</div><p class="desc">Ricotta cheese soaked in sweetened, thickened milk delicately flavored with cardamom</p></div>
      <div class="item"><div class="row">Kulfi<span class="fill"></span>$4.00</div><p class="desc">saffron and cinnamon topped w/ pistachios. Perfect treat after a great big meal!</p></div>
      <div class="item"><div class="row">Mango Ice-Cream<span class="fill"></span>$4.00</div><p class="desc">Lush tropical fruit makes a refreshing ice cream. Perfect treat for your taste buds!</p></div>
    </section>
    <div class="photo sweets" role="img" aria-label="Photo of Indian desserts in small bowls with a spoon"></div>
    <section>
      <h2 class="heading">Beverages</h2>
      <div class="item"><div class="row">Masala Tea<span class="fill"></span>$2.00</div><p class="desc">Indian Tea boiled w/ cinnamon, clove, Cardamom &amp; milk</p></div>
      <div class="item"><div class="row">Coffee<span class="fill"></span>$2.00</div></div>
      <div class="item"><div class="row">Tea<span class="fill"></span>$1.50</div></div>
      <div class="item"><div class="row">Soft Drinks<span class="fill"></span>$2.25</div><p class="desc">Cola, Diet Cola, Lemon-Lime, Orange, Lemonade &amp; Iced Tea</p></div>
      <div class="item"><div class="row">Lassi Mango<span class="fill"></span>$3.00</div><p class="desc">A cool mango yogurt smoothie</p></div>
      <div class="item"><div class="row">Lassi Plain<span class="fill"></span>$2.50</div><p class="desc">A cool drink plain yogurt, sweet or salted</p></div>
    </section>
  </div>

  <footer class="band">
    <div class="band-brand"><span class="dot"></span>Brisk Lark</div>
    <div class="band-phone">855 4 Lark Now! (855-555-0147)</div>
    <div class="band-web">You can order online, too: www.brisklarkmeals.com</div>
  </footer>
</div>
</body>
</html>
```